Haverlund’s First Annual Tree Fort Poker Tournament

Need a flyer made up of all the details. I like this tree fort image I uploaded with maybe 4-5 guys hanging out holding cards with some poker chips flying around. The name of it above it and then have the date, food provided over $10,000 in prize money, $500 buy in. Saturday December 17th, noon - ? 1/2 due by October 1 rest due day of tournament. Then have my contact info along with the guy helping me. Gregory Haverlund 314-617-3042 or Marcus Tredwin 314-586-2197

```html
<!DOCTYPE html>
<html lang="en">
<head>
<meta charset="utf-8">
<title>Haverlund’s First Annual Tree Fort Poker Tournament</title>
<link rel="stylesheet" href="https://fonts.googleapis.com/css2?family=Bebas+Neue&family=Oswald:wght@500;600&family=Montserrat:wght@700;800&display=swap">
<style>
  :root {
    --felt-top: #2a6a2a;
    --felt-mid: #1b4a1c;
    --felt-bottom: #141814;
    --sign-red: #b8261a;
    --sign-deep: #7a130d;
    --sign-rim: #e0641c;
    --bulb: #ffd36a;
    --gold: #e6b84a;
    --white: #ffffff;
    --prize-red: #e5161b;
    --buy-yellow: #ffe21a;
    --date-blue: #19a6e8;
    --pill-red: #e3141b;
    --pill-yellow: #ffe600;
    --ink: #1a1a1a;
    --page: #ffffff;
  }
  * { margin: 0; padding: 0; box-sizing: border-box; }
  html, body { width: 1200px; height: 2326px; overflow: hidden; background: var(--page); }
  .canvas { position: relative; width: 1200px; height: 2326px; }
  .flyer {
    position: absolute; left: 0; top: 314px; width: 1200px; height: 1697px; overflow: hidden;
    background: radial-gradient(ellipse 90% 60% at 50% 30%, var(--felt-top), var(--felt-mid) 55%, var(--felt-bottom) 100%);
  }
  .sign { position: absolute; left: 0; top: 0; width: 1200px; height: 900px; }
  .tree-fort {
    position: absolute; left: 0; top: 855px; width: 473px; height: 840px;
    background: linear-gradient(180deg, #5fae3a 0%, #4a8f2c 38%, #a9773f 60%, #6e4524 100%);
    border-radius: 46% 46% 8px 8px / 28% 28% 8px 8px;
    opacity: .9;
  }
  .player-photo {
    position: absolute; left: 560px; top: 806px; width: 405px; height: 551px;
    background: radial-gradient(ellipse 70% 60% at 50% 45%, #8a6a52, #4a3a2e 55%, rgba(30,40,35,0) 100%);
  }
  .details { position: absolute; left: 0; top: 0; width: 1200px; height: 1697px; color: var(--white); }
  .abs { position: absolute; white-space: nowrap; line-height: 1; }
  .lead { left: 479px; top: 1350px; font: 500 36px 'Oswald', sans-serif; transform: scaleX(.86); transform-origin: left; }
  .prize { left: 476px; top: 1386px; font: 600 104px 'Oswald', sans-serif; color: var(--prize-red); transform: scaleX(.86); transform-origin: left; }
  .prize-note { left: 479px; top: 1495px; font: 500 56px 'Oswald', sans-serif; transform: scaleX(.78); transform-origin: left; }
  .divider { position: absolute; left: 820px; top: 1365px; width: 2px; height: 190px; background: var(--white); }
  .buy-in { left: 836px; top: 1362px; font: 400 70px 'Bebas Neue', sans-serif; color: var(--buy-yellow); }
  .day { left: 902px; top: 1444px; font: 800 19px 'Montserrat', sans-serif; }
  .date { left: 836px; top: 1468px; font: 800 19px 'Montserrat', sans-serif; color: var(--date-blue); }
  .date sup { font-size: 11px; }
  .date-bar { position: absolute; left: 1044px; top: 1445px; width: 2px; height: 46px; background: var(--white); }
  .time { left: 1056px; top: 1442px; font: 400 54px 'Bebas Neue', sans-serif; color: var(--prize-red); }
  .terms { left: 836px; top: 1504px; font: 800 18.5px 'Montserrat', sans-serif; line-height: 1.35; }
  .rule { position: absolute; left: 479px; top: 1565px; width: 670px; height: 2px; background: var(--white); opacity: .85; }
  .contact-lead { left: 483px; top: 1578px; font: 800 18px 'Montserrat', sans-serif; }
  .contacts { position: absolute; left: 466px; top: 1603px; width: 681px; height: 53px; display: flex; border-radius: 27px; overflow: hidden; }
  .contact { display: flex; align-items: center; justify-content: center; white-space: nowrap; font: 500 24px 'Oswald', sans-serif; line-height: 1; }
  .contact span { display: inline-block; white-space: nowrap; transform: scaleX(.85); }
  .contact--red { flex: 0 0 372px; background: var(--pill-red); color: var(--white); padding-right: 20px; }
  .contact--yellow { flex: 1 1 auto; background: var(--pill-yellow); color: var(--ink); padding-left: 20px; }
  .or-badge {
    position: absolute; left: 354px; top: 8px; width: 37px; height: 37px; border-radius: 50%;
    background: var(--ink); color: var(--white); border: 2px solid var(--white);
    font: 800 14px 'Montserrat', sans-serif; display: flex; align-items: center; justify-content: center;
  }
</style>
</head>
<body>
<div class="canvas">
  <main class="flyer">
    <svg class="sign" viewBox="0 0 1200 900" aria-label="Haverlund’s First Annual Tree Fort Poker Tournament">
      <defs>
        <radialGradient id="signFace" cx="50%" cy="48%" r="60%">
          <stop offset="0" stop-color="#e2381f"/>
          <stop offset=".6" stop-color="var(--sign-red)"/>
          <stop offset="1" stop-color="var(--sign-deep)"/>
        </radialGradient>
        <linearGradient id="goldType" x1="0" y1="0" x2="0" y2="1">
          <stop offset="0" stop-color="#f7dc86"/>
          <stop offset=".5" stop-color="var(--gold)"/>
          <stop offset="1" stop-color="#b8862c"/>
        </linearGradient>
      </defs>
      <polygon class="sign-rim" points="606,168 1006,292 1006,738 606,857 206,738 206,292" fill="var(--sign-rim)"/>
      <polygon class="sign-face" points="606,190 986,306 986,724 606,836 226,724 226,306" fill="url(#signFace)"/>
      <polygon class="sign-bulbs" points="606,179 996,299 996,731 606,846 216,731 216,299" fill="none" stroke="var(--bulb)" stroke-width="6" stroke-linecap="round" stroke-dasharray="0 17"/>
      <text x="606" y="500" text-anchor="middle" font-family="'Bebas Neue', sans-serif" font-size="230" textLength="640" lengthAdjust="spacingAndGlyphs" fill="url(#goldType)">HAVERLUND’S</text>
      <text x="606" y="546" text-anchor="middle" font-family="'Montserrat', sans-serif" font-weight="800" font-size="34" textLength="650" lengthAdjust="spacingAndGlyphs" fill="var(--white)">FIRST ANNUAL TREE FORT POKER</text>
      <text x="606" y="752" text-anchor="middle" font-family="'Bebas Neue', sans-serif" font-size="215" textLength="650" lengthAdjust="spacingAndGlyphs" fill="var(--white)">TOURNAMENT</text>
    </svg>

    <div class="tree-fort" role="img" aria-label="Illustrated tree fort with ladder and tire swing"></div>
    <div class="player-photo" role="img" aria-label="Photo of a young player holding a fan of playing cards"></div>

    <section class="details">
      <p class="abs lead">FOOD PROVIDED OVER</p>
      <p class="abs prize">$10,000</p>
      <p class="abs prize-note">IN PRIZE MONEY</p>
      <div class="divider"></div>
      <p class="abs buy-in">$500 BUY IN</p>
      <p class="abs day">SATURDAY,</p>
      <p class="abs date">17<sup>TH</sup>DECEMBER</p>
      <div class="date-bar"></div>
      <p class="abs time">NOON</p>
      <p class="abs terms">1/2 DUE BY OCTOBER 1 REST<br>DUE DAY OF TOURNAMENT</p>
      <div class="rule"></div>
      <p class="abs contact-lead">THEN HAVE MY CONTACT INFO ALONG WITH THE GUY HELPING ME</p>
      <div class="contacts">
        <p class="contact contact--red"><span>GREGORY HAVERLUND 314-617-3042</span></p>
        <p class="contact contact--yellow"><span>MARCUS TREDWIN 314-586-2197</span></p>
        <span class="or-badge">OR</span>
      </div>
    </section>
  </main>
</div>
</body>
</html>
```